Business Cards for Law Office of Denise R. Harlow

I need a business card for my new estate planning law firm. I have attached my logo. I would like a design that is professional but not too formal or stuffy.

Target Market(s)

Professionals (lawyers, doctors, businesswomen) between the age of 30 and 50 who are tech-savvy and educated.

Industry/Entity Type

Lawyer

Contact Information for Business Card

Denise R. Harlow

528 E. 19th Street
7th Floor
New York, NY 10583

Phone: (855) 602-7318
Direct: (917) 463-5071
Email: Denise@DeniseRHarlowLegal.test
www.DeniseRHarlowLegal.test

Font styles to use
Other font styles liked:
• Corbel

Requirements
Must have
• On the front:
• Denise R. Harlow, Esq.
• Owner & Founder
• 528 E. 19th Street
• 7th Floor
• New York, NY 10583
• Phone: (855) 602-7318
• Direct: (917) 463-5071
• Email: denise@deniserharlowlegal.test
• www.deniserharlowlegal.test
• On the back:
• LOGO
Nice to have
• I want it to be professional but not too formal or stuffy. Please choose colors that go with my logo.
Should not have
• I don't want TOO MUCH color. Some color is good, but not too much.

```html
<!DOCTYPE html>
<html lang="en">
<head>
<meta charset="utf-8">
<title>Business Cards – Law Office of Denise R. Harlow</title>
<link rel="stylesheet" href="https://fonts.googleapis.com/css2?family=Open+Sans:wght@400;600;700&display=swap">
<style>
  :root {
    --backdrop: #2a2a2c;
    --paper: #ffffff;
    --purple: #74287a;
    --purple-dark: #5e1f63;
    --orange: #f07f1e;
    --orange-dark: #c95f1a;
    --orange-light: #f7a04a;
    --text-light: #ffffff;
    --shadow: rgba(0, 0, 0, 0.45);
  }
  * { box-sizing: border-box; margin: 0; padding: 0; }
  html, body {
    width: 1200px;
    height: 925px;
    overflow: hidden;
    background: var(--backdrop);
    font-family: "Open Sans", "Segoe UI", sans-serif;
  }
  .stage {
    width: 1200px;
    height: 925px;
    display: flex;
    align-items: center;
    justify-content: center;
    gap: 48px;
  }
  .card {
    position: relative;
    width: 540px;
    height: 309px;
    background: var(--paper);
    box-shadow: 0 18px 40px var(--shadow);
    overflow: hidden;
  }

  /* Logo side */
  .brand {
    position: absolute;
    display: flex;
    align-items: center;
    gap: 12px;
    color: var(--purple);
    font-weight: 600;
    white-space: nowrap;
  }
  .brand-mark {
    width: 12px;
    height: 12px;
    border-radius: 50%;
    background: var(--orange);
    flex: none;
  }
  .card-back .brand {
    left: 0; right: 0; top: 0; bottom: 0;
    justify-content: center;
    font-size: 25px;
    letter-spacing: 0.5px;
  }

  /* Contact side */
  .contact-panel {
    position: absolute;
    left: 0; top: 0;
    width: 100%;
    height: 186px;
    background: var(--purple);
    color: var(--text-light);
    padding: 22px 28px 0 116px;
  }
  .holder-name {
    font-size: 17px;
    font-weight: 700;
    line-height: 1.2;
  }
  .holder-title {
    font-size: 13px;
    color: var(--orange);
    margin-bottom: 8px;
  }
  .contact-columns {
    display: flex;
    gap: 24px;
  }
  .contact-list {
    list-style: none;
    font-size: 12px;
    line-height: 1.5;
    white-space: nowrap;
  }
  .address {
    font-style: normal;
    font-size: 12px;
    line-height: 1.5;
    align-self: flex-end;
    white-space: nowrap;
  }
  .accent-band {
    position: absolute;
    left: 0; top: 186px;
    width: 100%;
    height: 30px;
    background: linear-gradient(90deg,
      var(--orange) 0 6%, var(--orange-dark) 6% 11%, var(--orange) 11% 70%,
      var(--orange-light) 70% 76%, var(--orange-dark) 76% 82%,
      var(--orange) 82% 90%, var(--orange-light) 90% 100%);
    border-top: 3px solid var(--purple-dark);
    border-bottom: 3px solid var(--purple-dark);
  }
  .icon-pill {
    position: absolute;
    left: 28px; top: 2px;
    width: 106px;
    height: 20px;
    border-radius: 10px;
    background: var(--purple);
    display: flex;
    align-items: center;
    justify-content: space-evenly;
  }
  .icon-pill svg { width: 13px; height: 13px; }
  .card-front .brand {
    left: 0; right: 0; top: 216px; bottom: 0;
    justify-content: center;
    font-size: 17px;
  }
  .card-front .brand-mark { width: 9px; height: 9px; }
</style>
</head>
<body>
<main class="stage">
  <section class="card card-back" aria-label="Card back">
    <div class="brand"><span class="brand-mark"></span>Law Office of Denise R. Harlow</div>
  </section>

  <section class="card card-front" aria-label="Card front">
    <div class="contact-panel">
      <h1 class="holder-name">Denise R. Harlow, Esq.</h1>
      <p class="holder-title">Owner &amp; Founder</p>
      <div class="contact-columns">
        <ul class="contact-list">
          <li>(855) 602-7318</li>
          <li>(917) 463-5071</li>
          <li>denise@deniserharlowlegal.test</li>
          <li>www.deniserharlowlegal.test</li>
        </ul>
        <address class="address">
          528 E. 19th Street<br>
          7th Floor, New York, NY 10583
        </address>
      </div>
    </div>

    <div class="accent-band">
      <div class="icon-pill">
        <svg viewBox="0 0 16 16" aria-label="Mobile"><rect x="4.5" y="1.5" width="7" height="13" rx="1.5" fill="none" stroke="#f07f1e" stroke-width="1.5"/><circle cx="8" cy="12" r="0.9" fill="#f07f1e"/></svg>
        <svg viewBox="0 0 16 16" aria-label="Phone"><path d="M4 2l2.5 3-1.5 1.5c.8 1.8 2.2 3.2 4 4L10.5 9 13.5 11.5 12 14C7 13.5 2.5 9 2 4z" fill="#f07f1e"/></svg>
        <svg viewBox="0 0 16 16" aria-label="Email"><rect x="1.5" y="3.5" width="13" height="9" fill="none" stroke="#f07f1e" stroke-width="1.5"/><path d="M1.5 3.5L8 9l6.5-5.5" fill="none" stroke="#f07f1e" stroke-width="1.5"/></svg>
        <svg viewBox="0 0 16 16" aria-label="Website"><circle cx="8" cy="8" r="6" fill="none" stroke="#f07f1e" stroke-width="1.4"/><ellipse cx="8" cy="8" rx="2.6" ry="6" fill="none" stroke="#f07f1e" stroke-width="1.1"/><path d="M2 8h12" stroke="#f07f1e" stroke-width="1.1"/></svg>
      </div>
    </div>

    <div class="brand"><span class="brand-mark"></span>Law Office of Denise R. Harlow</div>
  </section>
</main>
</body>
</html>
```